Rin3Vox Header

I want a professional Letterhead for my law firm. I'm attaching the letterhead I currently use in Word and PDF form. I'm also attaching my logo, and an example header that I like.

```html
<!DOCTYPE html>
<html lang="en">
<head>
<meta charset="utf-8">
<title>Rin3Vox Letterhead</title>
<link rel="stylesheet" href="https://fonts.googleapis.com/css2?family=Noto+Serif:wght@300;400&family=Noto+Sans:ital,wght@0,400;0,700;0,800;1,400&display=swap">
<style>
  :root {
    --cyan: #1aa9db;
    --green: #3f7d3f;
    --ink: #222222;
    --ink-soft: #333333;
    --paper: #fcfcfc;
  }
  * { margin: 0; padding: 0; box-sizing: border-box; }
  html, body { width: 1100px; height: 1200px; overflow: hidden; background: var(--paper); }
  body { font-family: "Noto Sans", sans-serif; color: var(--ink); font-size: 17px; }
  .letterhead { position: relative; width: 1100px; height: 1200px; background: var(--paper); }

  .brand { position: absolute; left: 74px; top: 70px; display: flex; align-items: center; gap: 10px; }
  .brand-mark { width: 18px; height: 18px; background: var(--cyan); }
  .brand-name { font-size: 54px; font-weight: 800; color: var(--ink); letter-spacing: -1px; line-height: 1; }

  .header-rule { position: absolute; left: 390px; right: 74px; top: 92px; height: 6px; background: var(--green); }

  .firm-name { position: absolute; right: 74px; top: 50px; font-family: "Noto Serif", serif; font-weight: 300; font-size: 27px; color: var(--cyan); }
  .firm-title { position: absolute; right: 74px; top: 108px; font-size: 16px; color: var(--ink-soft); }

  .contact { position: absolute; right: 74px; top: 138px; font-size: 16px; color: var(--ink-soft); }
  .contact-grid { display: grid; grid-template-columns: auto auto; column-gap: 26px; row-gap: 4px; justify-items: end; }
  .contact-item { display: flex; align-items: center; gap: 10px; }
  .contact-item svg { width: 13px; height: 13px; fill: var(--cyan); }
  .contact-address { margin-top: 8px; display: flex; justify-content: flex-end; align-items: center; gap: 12px; }

  .meta { position: absolute; left: 74px; right: 74px; top: 242px; display: flex; justify-content: space-between; font-weight: 700; font-size: 17px; letter-spacing: 0.3px; }

  .recipient { position: absolute; left: 74px; top: 300px; font-size: 17px; line-height: 26px; font-style: normal; }
  .recipient strong { font-weight: 700; }

  .subject { position: absolute; left: 74px; right: 74px; top: 426px; text-align: center; font-size: 17px; line-height: 27px; }
  .subject-title { font-weight: 700; letter-spacing: 0.4px; }
  .subject-details b { font-weight: 700; }
  .subject-details .sep { margin: 0 8px; }

  .salutation { position: absolute; left: 74px; top: 506px; font-weight: 700; font-size: 17px; }

  .body-copy { position: absolute; left: 74px; right: 74px; top: 546px; font-size: 17px; line-height: 26px; text-align: justify; }
  .body-copy p + p { margin-top: 26px; }

  .closing { position: absolute; left: 74px; top: 858px; font-size: 17px; }
  .signature { position: absolute; left: 74px; top: 884px; width: 210px; height: 68px; background: linear-gradient(90deg, rgba(26,169,219,0.18), rgba(26,169,219,0.05)); }
  .signer { position: absolute; left: 74px; top: 956px; font-size: 17px; line-height: 25px; }
  .signer-name { font-weight: 700; }
  .signer-role { font-style: italic; }

  .footer-bands { position: absolute; left: 0; right: 0; bottom: 28px; }
  .band-cyan { height: 7px; background: var(--cyan); }
  .band-green { height: 6px; margin-top: 3px; background: var(--green); }
</style>
</head>
<body>
<main class="letterhead">
  <header>
    <div class="brand">
      <span class="brand-mark"></span>
      <span class="brand-name">Rin3Vox</span>
    </div>
    <div class="header-rule"></div>
    <div class="firm-name">Casimir D. Arroyo III</div>
    <div class="firm-title">Attorney at Law, PLLC</div>
    <div class="contact">
      <div class="contact-grid">
        <div class="contact-item">(877) 555-0142
          <svg viewBox="0 0 16 16"><circle cx="8" cy="8" r="7"/></svg></div>
        <div class="contact-item">cas@rin3vox.com
          <svg viewBox="0 0 16 16"><path d="M1 3h14v10H1z M1 3l7 6 7-6"/></svg></div>
        <div class="contact-item">(469) 555-0187
          <svg viewBox="0 0 16 16"><path d="M3 2l3 1 1 3-2 1a8 8 0 0 0 4 4l1-2 3 1 1 3-2 1C7 14 2 9 2 4z"/></svg></div>
        <div class="contact-item">www.rin3vox.com
          <svg viewBox="0 0 16 16"><circle cx="8" cy="8" r="7"/></svg></div>
      </div>
      <div class="contact-address">2740 Harwood Ln. Ste 210 Dallas, TEXAS 75204
        <svg width="12" height="15" viewBox="0 0 12 16" fill="var(--cyan)"><path d="M6 0a6 6 0 0 0-6 6c0 4 6 10 6 10s6-6 6-10a6 6 0 0 0-6-6zm0 8.5A2.5 2.5 0 1 1 6 3.5a2.5 2.5 0 0 1 0 5z"/></svg>
      </div>
    </div>
  </header>

  <div class="meta">
    <span>VIA FACSIMILE : (800)-555-0119</span>
    <span>July &nbsp;&nbsp;11, 2021</span>
  </div>

  <address class="recipient">
    <div><strong>Attn:</strong> Peter Lindqvist</div>
    <div><strong>Harborline Insurance</strong></div>
    <div>4820 Belt Line Rd 300 Dallas, Texas 75240</div>
    <div>Tel: (972)-555-0164</div>
  </address>

  <section class="subject">
    <div class="subject-title">RE : NOTICE OF &nbsp;REPRESENTATION</div>
    <div class="subject-details">Claim Number: &nbsp;<b>2084396-TX</b><span class="sep">|</span>Date of Accident: &nbsp;<b>February 3, 2018</b><span class="sep">|</span>My client: <b>Jane Roe</b></div>
  </section>

  <div class="salutation">Dear Mr. Peter Lindqvist,</div>

  <section class="body-copy">
    <p>Lorem Ipsum is simply dummy text of the printing and typesetting industry. Lorem Ipsum has been the industry's standard dummy text ever since the 1500s, when an unknown printer took a galley of type and scrambled it to make a type specimen book. It has survived not only five centuries, but also the leap into electronic typesetting, remaining essentially unchanged. It was popularised in the 1960s with the release of Typeshift sheets containing Lorem Ipsum passages, and more recently with desktop publishing software like Quillset Layout including versions of Lorem Ipsum.</p>
    <p>Lorem Ipsum is simply dummy text of the printing and typesetting industry. Lorem Ipsum has been the industry's standard dummy text ever since the 1500s, when an unknown printer took a galley of type and scrambled it to make a type specimen book. It has survived not only five centuries, but also the leap into electronic typesetting, remaining essentially unchanged. I</p>
  </section>

  <div class="closing">Sincerely,</div>
  <div class="signature" role="img" aria-label="Handwritten signature of the attorney in blue ink"></div>
  <div class="signer">
    <div class="signer-name">Casimir D. Arroyo</div>
    <div class="signer-role">Attorney at Law</div>
  </div>

  <footer class="footer-bands">
    <div class="band-cyan"></div>
    <div class="band-green"></div>
  </footer>
</main>
</body>
</html>
```